Robotic startup business cards

We are looking for a design for a set of business cards which reflect the spirit and humor of Vortalo Robotics. We want to present ourselves as sleek, professional, but laid-back consulting company.

We primarily focus on developing robotic arms software. This software controls robots and does things like grab items, pick objects up, move them, etc.

We want to allow you maximum design creativity, but do ask that you consider our existing style guidelines (see attached files) in order to make our brand cohesive.

Target Market(s)

Startups and Mid-size robotic companies

Industry/Entity Type

Business

Contact Information for Business Card

Miro Halvensky, PhD
Roboticist | Vortalo Consulting | 318.570.9164

Font styles to use
Other font styles liked:
• Source code pro

Requirements
Must have
• robots or robotic arms
• similar color scheme that works with existing brand guidelines
Nice to have
• please consider our existing style guidelines (see attached files) in order to make our brand cohesive.
• minimalism style is generally nice.
Should not have
• An old, boring, or corporate feel. Too much text.

```html
<!DOCTYPE html>
<html lang="en">
<head>
<meta charset="utf-8">
<title>Vortalo Robotics — Business Cards</title>
<link rel="stylesheet" href="https://fonts.googleapis.com/css2?family=Source+Code+Pro:wght@300&family=Arimo:wght@400;700&display=swap">
<style>
  :root {
    --stage: #555555;
    --card-white: #ffffff;
    --brand-green: #05e6a0;
    --ink: #222222;
    --wordmark-ink: #2a2a2a;
    --robot-tone-light: #f1f1f1;
    --robot-tone-mid: #e4e4e4;
    --robot-tone-accent: #f6dede;
    --card-shadow: rgba(0, 0, 0, 0.45);
  }
  * { margin: 0; padding: 0; box-sizing: border-box; }
  html, body { width: 1200px; height: 900px; overflow: hidden; }
  body {
    background: var(--stage);
    position: relative;
    font-family: "Arimo", Arial, sans-serif;
  }
  .card {
    position: absolute;
    top: 170px;
    width: 347px;
    height: 561px;
    overflow: hidden;
    box-shadow: 2px 3px 4px var(--card-shadow);
  }
  .card--front { left: 259px; background: var(--card-white); }
  .card--back { left: 631px; background: var(--brand-green); }

  .robot-illustration {
    position: absolute;
    left: 228px;
    top: 10px;
    width: 140px;
    height: 551px;
    border-radius: 60px 0 0 40px;
    background: linear-gradient(180deg,
      var(--robot-tone-mid) 0%,
      var(--robot-tone-light) 35%,
      var(--robot-tone-accent) 55%,
      var(--robot-tone-light) 75%,
      var(--robot-tone-mid) 100%);
    opacity: 0.8;
  }

  .brand-lockup {
    position: absolute;
    left: 37px;
    top: 148px;
    display: flex;
    align-items: center;
    gap: 26px;
  }
  .brand-dot {
    width: 26px;
    height: 26px;
    border-radius: 50%;
    background: var(--brand-green);
  }
  .wordmark {
    font-family: "Source Code Pro", "Courier New", monospace;
    font-weight: 300;
    letter-spacing: 6px;
    color: var(--wordmark-ink);
  }
  .brand-lockup .wordmark { font-size: 34px; }

  .contact {
    position: absolute;
    left: 0;
    width: 347px;
    top: 352px;
    text-align: center;
    color: var(--ink);
    font-size: 16px;
    line-height: 21px;
  }
  .contact__name {
    color: var(--brand-green);
    font-weight: 700;
    font-size: 20px;
    line-height: 26px;
  }
  .contact__degree { font-weight: 400; }
  .contact__role { margin-bottom: 29px; }
  .contact__company {
    color: var(--brand-green);
    font-weight: 700;
    font-size: 18px;
    line-height: 24px;
    margin-bottom: 8px;
  }

  .back-circle {
    position: absolute;
    left: 130px;
    top: 190px;
    width: 62px;
    height: 62px;
    border-radius: 50%;
    background: rgba(0, 0, 0, 0.08);
  }
  .card--back .wordmark {
    position: absolute;
    left: 0;
    width: 347px;
    top: 452px;
    text-align: center;
    font-size: 52px;
    color: var(--card-white);
    letter-spacing: 7px;
  }
</style>
</head>
<body>
  <section class="card card--front" aria-label="Business card front">
    <div class="robot-illustration" role="img" aria-label="Faint illustration of a friendly robot with a red robotic arm"></div>
    <div class="brand-lockup">
      <span class="brand-dot"></span>
      <span class="wordmark">VORTALO</span>
    </div>
    <div class="contact">
      <p class="contact__name">MIRO HALVENSKY, <span class="contact__degree">PhD</span></p>
      <p class="contact__role">ROBOTICIST</p>
      <p class="contact__company">VORTALO CONSULTING</p>
      <p class="contact__phone">318.570.9164</p>
      <p class="contact__email">INFO@WEBSITENAME.COME</p>
    </div>
  </section>

  <section class="card card--back" aria-label="Business card back">
    <span class="back-circle"></span>
    <span class="wordmark">VORTALO</span>
  </section>
</body>
</html>
```